truck and trailer business Wrap Design

needing a redisgn of our truck and trailer wraps, i have attached the current trailer wrap design and pictures of the new trailer needing a wrap design. trailer is 26ft v nose. 8.5 wide and 7.5ft tall need the trucks that pull the trailers to match. 2018 r-380 long bed. i have attached pictures of the truck. 2009 ZOBI 26 FT BOX
Updates

Low design quality

Industry/Entity Type

Insulation

Colors

Designer to choose colors to be used in the design.

Requirements
Must have
• wrap needs to be unique and stand out like our current wrap

```html
<!DOCTYPE html>
<html lang="en">
<head>
<meta charset="utf-8">
<title>Apex Spray Foam – Box Truck Wrap</title>
<link href="https://fonts.googleapis.com/css2?family=Exo+2:ital,wght@0,800;1,700;1,800&display=swap" rel="stylesheet">
<style>
  :root {
    --ink: #0b0c0f;
    --charcoal: #2a2d33;
    --steel: #4a4f57;
    --brand-blue: #0d3f7a;
    --bright-blue: #1f6fd1;
    --white: #ffffff;
    --paper: #eef0f3;
    --pale: #d8dde3;
  }
  * { box-sizing: border-box; margin: 0; padding: 0; }
  html, body { width: 1200px; height: 1200px; overflow: hidden; }
  body {
    background: var(--paper);
    font-family: "Exo 2", sans-serif;
    color: var(--white);
    position: relative;
  }
  .panel {
    position: absolute;
    background: linear-gradient(90deg, var(--ink) 0%, var(--charcoal) 45%, var(--ink) 70%, var(--steel) 100%);
    overflow: hidden;
  }
  /* ---------- side panel ---------- */
  .side { left: 40px; top: 40px; width: 1120px; height: 340px; }
  .side .job-photo {
    position: absolute; inset: 0;
    background: linear-gradient(100deg, #f3f1ec 0%, #cfc7b8 30%, #8a6c4c 55%, #e9e6df 80%);
    clip-path: polygon(0 0, 30% 0, 44% 100%, 0 100%);
  }
  .side .web-bar {
    position: absolute; left: 30px; top: 232px; width: 470px; height: 52px;
    background: var(--brand-blue);
    clip-path: polygon(0 0, 94% 0, 100% 100%, 0 100%);
    display: flex; align-items: center; padding-left: 40px;
    font-style: italic; font-weight: 800; font-size: 22px; letter-spacing: .5px;
  }
  .side .brand {
    position: absolute; left: 440px; top: 30px; width: 640px;
    text-align: center;
  }
  .rule { height: 3px; background: var(--pale); margin: 0 auto; }
  .side .brand .rule { width: 600px; }
  .brand-name {
    font-weight: 800; font-size: 58px; line-height: 1; letter-spacing: 3px;
    color: var(--white); padding: 16px 0 14px;
  }
  .side .services {
    position: absolute; left: 400px; right: 0; top: 168px; height: 40px;
    background: var(--brand-blue);
    clip-path: polygon(3% 0, 100% 0, 100% 100%, 0 100%);
    display: flex; align-items: center; justify-content: center;
    font-style: italic; font-weight: 800; font-size: 19px; letter-spacing: 1px;
  }
  .side .phone {
    position: absolute; right: 60px; top: 212px;
    font-style: italic; font-weight: 800; font-size: 62px; letter-spacing: 2px;
  }
  .social {
    display: flex; align-items: center; gap: 8px;
    font-style: italic; font-weight: 700; color: var(--bright-blue);
  }
  .social .mark { width: 14px; height: 14px; background: var(--bright-blue); }
  .side .social { position: absolute; left: 500px; top: 290px; font-size: 14px; }
  .tagline { font-style: italic; font-weight: 800; color: var(--white); }
  .tagline span { color: var(--brand-blue); }
  .side .tagline { position: absolute; left: 500px; top: 312px; font-size: 11px; }

  /* ---------- front header ---------- */
  .front { left: 40px; top: 440px; width: 520px; height: 150px; background: var(--ink); text-align: center; padding-top: 24px; }
  .front .url { font-style: italic; font-weight: 800; font-size: 20px; letter-spacing: 1px; }
  .front .rule { width: 400px; height: 2px; margin-top: 12px; }
  .front .brand-name { font-size: 30px; padding: 8px 0; }

  /* ---------- rear door ---------- */
  .rear { left: 620px; top: 440px; width: 540px; height: 720px; text-align: center; }
  .rear .brand { margin-top: 80px; }
  .rear .rule { width: 480px; }
  .rear .brand-name { font-size: 44px; padding: 14px 0 12px; }
  .rear .tagline { font-size: 19px; margin-top: 40px; }
  .rear .phone-band {
    margin-top: 60px; height: 90px; background: var(--brand-blue);
    display: flex; align-items: center; justify-content: center;
    font-style: italic; font-weight: 800; font-size: 58px; letter-spacing: 2px;
  }
  .rear .services {
    margin-top: 44px; font-style: italic; font-weight: 800; font-size: 30px; line-height: 1.3; letter-spacing: 1px;
  }
  .rear .social { justify-content: center; margin-top: 34px; font-size: 22px; }
  .rear .social .mark { width: 22px; height: 22px; }
  .rear .url { margin-top: 22px; font-style: italic; font-weight: 800; font-size: 21px; letter-spacing: .5px; }
</style>
</head>
<body>

<section class="panel side">
  <div class="job-photo" role="img" aria-label="Photo of installers in protective suits spraying foam insulation between wall studs"></div>
  <div class="web-bar">APEXSPRAYFOAM.NET</div>
  <div class="brand">
    <div class="rule"></div>
    <div class="brand-name">APEX SPRAY FOAM</div>
    <div class="rule"></div>
  </div>
  <div class="services">SPRAY FOAM - FIBERGLASS - INSULATION - ROOFING</div>
  <div class="phone">555-010-4827</div>
  <div class="social"><span class="mark"></span>APEXSPRAYFOAM</div>
  <div class="tagline">DFW <span>PREMIER</span> INSULATION <span>COMPANY</span></div>
</section>

<section class="panel front">
  <div class="url">APEXSPRAYFOAM.NET</div>
  <div class="rule"></div>
  <div class="brand-name">APEX SPRAY FOAM</div>
  <div class="rule"></div>
</section>

<section class="panel rear">
  <div class="brand">
    <div class="rule"></div>
    <div class="brand-name">APEX SPRAY FOAM</div>
    <div class="rule"></div>
  </div>
  <div class="tagline">DFW <span>PREMIER</span> INSULATION <span>COMPANY</span></div>
  <div class="phone-band">555-010-4827</div>
  <div class="services">SPRAY FOAM - FIBERGLASS<br>INSULATION - ROOFING</div>
  <div class="social"><span class="mark"></span>APEXSPRAYFOAM</div>
  <div class="url">APEXSPRAYFOAM.NET</div>
</section>

</body>
</html>
```